ORLUq Business card. A.I. company developing trading strategies.

My name is tommaso fabbri and I'm CEO and co-founder of ORLUQ Research, an AI company focusing on generating Ai-driven trading strategies.
This is our website: https://orluq-research.example/
Values of our company: tech & R&D driven (we're all very mathy/stats/data driven), sophisticated (we only look for sophisticated, high knowledge investors), reserved (we don't go around telling anyone what we do).
Our main product: KobraFNX. A trading strategy that delivered 70% in 2022 and 20% in 2023 so far.
Our main potential clients: HNW individuals, hedge funds, asset managers, tech entrepreneur.
Hedge funds, asset managers, High Net Worth individuals, Pension funds
The basic: name, job title, company name, address, mail, phone number

```html
<!DOCTYPE html>
<html lang="en">
<head>
<meta charset="utf-8">
<title>ORLUq Research – Business Card</title>
<link rel="stylesheet" href="https://fonts.googleapis.com/css2?family=Montserrat:wght@400;500;700&display=swap">
<style>
  :root {
    --backdrop: #262626;
    --card: #161616;
    --card-edge: #1d1d1d;
    --ink: #f2f2f2;
    --ink-soft: #e4e4e4;
    --accent: #c8293f;
    --emboss: #2c2c2c;
  }
  * { box-sizing: border-box; margin: 0; padding: 0; }
  html, body {
    width: 1200px; height: 900px; overflow: hidden;
    background: var(--backdrop);
    font-family: "Montserrat", sans-serif;
  }
  .stage {
    width: 1200px; height: 900px;
    display: flex; flex-direction: column; align-items: center; justify-content: center;
    gap: 40px;
  }
  .card {
    width: 640px; height: 366px;
    background: linear-gradient(135deg, var(--card) 0%, var(--card-edge) 100%);
    position: relative;
    box-shadow: 0 6px 18px rgba(0,0,0,.35);
  }
  /* Front */
  .card--front { display: flex; align-items: center; justify-content: center; }
  .wordmark {
    font-weight: 500; letter-spacing: 6px;
    display: flex; align-items: center; gap: 14px;
  }
  .wordmark__dot { width: 10px; height: 10px; border-radius: 50%; }
  .card--front .wordmark { font-size: 64px; color: var(--emboss); }
  .card--front .wordmark__dot { background: var(--emboss); }
  /* Back */
  .card--back { display: flex; align-items: center; }
  .card__brand { width: 330px; display: flex; justify-content: center; }
  .card--back .wordmark { font-size: 56px; color: var(--ink); }
  .card--back .wordmark__dot { background: var(--accent); }
  .card__divider { width: 2px; height: 190px; background: var(--accent); }
  .contact { padding-left: 30px; color: var(--ink-soft); }
  .contact__name {
    color: var(--accent); font-weight: 700; font-size: 24px;
    text-transform: uppercase; letter-spacing: 1px;
  }
  .contact__title { font-size: 14px; margin-top: 2px; }
  .contact__address { font-size: 14px; line-height: 1.35; margin-top: 16px; }
  .contact__list { list-style: none; margin-top: 16px; font-size: 14px; }
  .contact__list li { display: flex; align-items: center; gap: 10px; margin-bottom: 6px; }
  .icon { width: 14px; height: 14px; flex: none; fill: var(--accent); }
</style>
</head>
<body>
<main class="stage">
  <section class="card card--front" aria-label="Card front">
    <div class="wordmark"><span>ORLUq</span><span class="wordmark__dot"></span></div>
  </section>

  <section class="card card--back" aria-label="Card back">
    <div class="card__brand">
      <div class="wordmark"><span>ORLUq</span><span class="wordmark__dot"></span></div>
    </div>
    <div class="card__divider"></div>
    <div class="contact">
      <h1 class="contact__name">Tommaso Fabbri</h1>
      <p class="contact__title">CEO and Co-Founder</p>
      <p class="contact__address">5475 Street Name<br>Country Name AB 8542</p>
      <ul class="contact__list">
        <li>
          <svg class="icon" viewBox="0 0 24 24" aria-hidden="true"><path d="M6.6 10.8a15.2 15.2 0 0 0 6.6 6.6l2.2-2.2a1 1 0 0 1 1-.25 11.4 11.4 0 0 0 3.6.57 1 1 0 0 1 1 1V20a1 1 0 0 1-1 1A17 17 0 0 1 3 4a1 1 0 0 1 1-1h3.5a1 1 0 0 1 1 1c0 1.25.2 2.45.57 3.57a1 1 0 0 1-.25 1z"/></svg>
          <span>123-555-0148</span>
        </li>
        <li>
          <svg class="icon" viewBox="0 0 24 24" aria-hidden="true"><path d="M2 5h20v14H2z M2 5l10 8 10-8" fill="var(--accent)"/><path d="M2 5l10 8 10-8" fill="none" stroke="#161616" stroke-width="1.6"/></svg>
          <span>info@orluq-research.example</span>
        </li>
        <li>
          <svg class="icon" viewBox="0 0 24 24" aria-hidden="true"><circle cx="12" cy="12" r="10"/><path d="M2 12h20M12 2c3 3 3 17 0 20M12 2c-3 3-3 17 0 20" fill="none" stroke="#161616" stroke-width="1.4"/></svg>
          <span>www.orluq-research.example</span>
        </li>
      </ul>
    </div>
  </section>
</main>
</body>
</html>
```